Clean, Fresh Business Card Design Needed

We need a business card design for a new business we have taken over called "Bonders and Fillers". We got a logo through this website which i have attached. We are wanting something that is vibrant but clean and fresh. Our business mainly sells glue. Maybe a cool design/slogan on the back? Modern, sleek.

Industry/Entity Type

Business

Contact Information for Business Card

Name: Ewan Tressider, Managing Director. Address: 164 Kelmond Road, Tauranga 3117, Phone: 07 462 3947 Mobile: 021 354 921 Fax: 07 462 5086 Email: bondfill.mail@pelorix.co.nz, Web: www.stickwarex.co.nz

Font styles to use
Serif

Requirements
Must have
• All business card details, logo.
Nice to have
• Design, slogan on back of card

```html
<!DOCTYPE html>
<html lang="en">
<head>
<meta charset="utf-8">
<title>Bonders and Fillers – Business Card</title>
<link rel="stylesheet" href="https://fonts.googleapis.com/css2?family=Crimson+Pro:wght@400;600;700&display=swap">
<style>
  :root {
    --backdrop: #d9d9de;
    --card: #ffffff;
    --card-shade: #ececec;
    --brand-blue: #4f5391;
    --brand-blue-dark: #2f3173;
    --brand-grey: #6a6a6a;
    --band-grey: #a8a8a8;
    --ink: #1e1e1e;
    --ink-soft: #4a4a4a;
  }
  * { box-sizing: border-box; margin: 0; padding: 0; }
  html, body {
    width: 1200px; height: 900px; overflow: hidden;
    background: var(--backdrop);
    font-family: "Crimson Pro", "Times New Roman", serif;
  }
  .canvas {
    position: relative; width: 1200px; height: 900px;
  }
  .card {
    position: absolute; left: 260px;
    width: 680px; height: 389px;
    background: linear-gradient(180deg, var(--card-shade) 0%, var(--card) 55%);
    box-shadow: 0 6px 18px rgba(0,0,0,0.18);
    overflow: hidden;
  }
  .card--back { top: 46px; }
  .card--front { top: 465px; }

  .brand { display: flex; align-items: center; gap: 16px; }
  .brand__mark { width: 70px; height: 70px; background: var(--brand-blue); flex: none; }
  .brand__name {
    font-size: 44px; font-weight: 400; color: var(--brand-grey);
    letter-spacing: 1px; line-height: 1;
  }

  /* back */
  .card--back .brand { position: absolute; left: 0; right: 0; top: 120px; justify-content: center; }
  .card--back .web {
    position: absolute; left: 0; right: 0; top: 210px; text-align: center;
    font-size: 20px; letter-spacing: 2.5px; color: var(--ink);
  }
  .band { position: absolute; bottom: 0; height: 24px; }
  .card--back .band--grey { left: 0; width: 250px; background: var(--band-grey); }
  .card--back .band--blue { left: 254px; right: 0; background: var(--brand-blue); }

  /* front */
  .card--front .brand { position: absolute; left: 40px; top: 36px; }
  .person {
    position: absolute; left: 40px; top: 150px;
    display: flex; align-items: baseline; gap: 10px;
  }
  .person__name { font-size: 27px; font-weight: 700; color: var(--brand-blue); }
  .person__role { font-size: 18px; letter-spacing: 1px; color: var(--ink-soft); }
  .rule {
    position: absolute; left: 38px; right: 0; top: 186px;
    height: 2px; background: var(--brand-blue-dark);
  }
  .contacts { position: absolute; left: 42px; top: 202px; list-style: none; }
  .contacts li {
    display: flex; align-items: center; gap: 16px;
    height: 28px; font-size: 18px; color: var(--ink-soft);
  }
  .contacts svg { width: 16px; height: 16px; fill: var(--ink-soft); flex: none; }
  .address {
    position: absolute; right: 44px; bottom: 38px; text-align: right;
    font-size: 19px; color: var(--ink); line-height: 1.3;
  }
  .address__company { font-weight: 700; }
  .card--front .band--blue { left: 0; width: 190px; background: var(--brand-blue); }
  .card--front .band--grey { left: 194px; right: 0; background: var(--band-grey); }
</style>
</head>
<body>
<main class="canvas">

  <section class="card card--back" aria-label="Card back">
    <div class="brand">
      <span class="brand__mark"></span>
      <span class="brand__name">Bonders and Fillers</span>
    </div>
    <p class="web">www.stickwarex.co.nz</p>
    <div class="band band--grey"></div>
    <div class="band band--blue"></div>
  </section>

  <section class="card card--front" aria-label="Card front">
    <div class="brand">
      <span class="brand__mark"></span>
      <span class="brand__name">Bonders and Fillers</span>
    </div>
    <div class="person">
      <span class="person__name">Ewan Tressider</span>
      <span class="person__role">MANAGER</span>
    </div>
    <div class="rule"></div>
    <ul class="contacts">
      <li>
        <svg viewBox="0 0 16 16" aria-hidden="true"><path d="M3 1h3l1.5 4-2 1.3a9 9 0 0 0 4.2 4.2L11 8.5l4 1.5v3a2 2 0 0 1-2 2A12 12 0 0 1 1 3a2 2 0 0 1 2-2z"/></svg>
        07 462 3947
      </li>
      <li>
        <svg viewBox="0 0 16 16" aria-hidden="true"><path d="M4 1h8v4H4zM1 6h14v6h-3v3H4v-3H1zM5 10v4h6v-4z"/></svg>
        07 462 5086
      </li>
      <li>
        <svg viewBox="0 0 16 16" aria-hidden="true"><path d="M4 0h8a1 1 0 0 1 1 1v14a1 1 0 0 1-1 1H4a1 1 0 0 1-1-1V1a1 1 0 0 1 1-1zm1 2v9h6V2zm3 10.5a1 1 0 1 0 0 2 1 1 0 0 0 0-2z"/></svg>
        021 354 921
      </li>
      <li>
        <svg viewBox="0 0 16 16" aria-hidden="true"><path d="M0 3h16v1L8 9 0 4zM0 5.5l8 5 8-5V13H0z"/></svg>
        bondfill.mail@pelorix.co.nz
      </li>
    </ul>
    <div class="address">
      <p class="address__company">Bonders and Fillers</p>
      <p>164 Kelmond Road, Tauranga 3117</p>
    </div>
    <div class="band band--blue"></div>
    <div class="band band--grey"></div>
  </section>

</main>
</body>
</html>
```